Children friendly theme required for simple Maths mobile app

Simply the app presents 100 random maths questions one-by-one that the child attempts to answer within a set time.

The title of the app is "Sum Rocket Drills"

See attached mock-up for further details.

Design elements required:

1. Color scheme: Reasonably colorful.

2. Logo: A stylized clock (with a single sweeping (blurred) hand or “alarm clock” style) with the plus, minus, divide and multiplication symbols and numbers spinning around it. The clock is the largest element with the operator symbols smaller and the number small again (numbers can be a mix of sizes). Logo should have square dimensions and needs to scale as large as 512px square and as small as 29px square. No words should be on the icon.

3. Background: All screens will have a common background containing all or parts of the logo in various sizes and positions. If time permits each screen can have a subtle variation of design (e.g.: slight color change etc).

4. Button with simple down-state. In the mock-up navigation buttons have greater-than/less-than symbols to imply direction/flow. This could instead be included in the button design (e.g.: button outline points more to the left or right). “For Parents” IS a button and will be rendered as text only.

5. Splash screen: Can just contain the title, logo and background.

6. Font: The app uses static and dynamic text so the font(s) used will need to be embedded in the app. I was considering using Comic Sans for the text (including the number keypad).

7. Graphics: The app uses two icons - a “star” and “clock” images/icons to indicate the top score and time-limit respectively for participants. The clock icon probably needs to be the same as the clock image in the logo (although this is not essential).

Important: Design needs to be children friendly but plain as visuals are not the focus.

Screen size will be 320 x 480, portrait only.

Files need to be submitted in 32-bit PNG format.

This is my first time using PixelHarbor and my first time formally specifying a design so please ask questions if anything is unclear.
Updates

Hi all,

Budget has been doubled based on advice from PixelHarbor and feedback from some potential designers.

Regards,
   Gregor

Hi all,

Sorry about a late change in the brief - the title of the app is now "Sum Rocket Drills".

Kind regards,
   Gregor

Target Market(s)

Parent/Teachers (but for children to use) – i.e.: This app will unlikely be discovered/downloaded by children.

Requirements
Nice to have
• Slightly different background for each screen. Screens are numbered 1 to 6 in the mockup.
Should not have
• "Overwhelming" or overpowering visuals. The task/content is the focus.

```html
<!DOCTYPE html>
<html lang="en">
<head>
<meta charset="utf-8">
<title>Sum Rocket Drills – App Screens</title>
<link href="https://fonts.googleapis.com/css2?family=Comic+Neue:wght@400;700&display=swap" rel="stylesheet">
<style>
  :root {
    --page-bg: #f3f4f6;
    --label-blue: #0f3a7a;
    --frame-yellow: #ffe600;
    --screen-blue: #1a73e8;
    --screen-blue-deep: #0b4fc4;
    --screen-blue-light: #3d9bff;
    --button-white: #ffffff;
    --ink-dark: #14213d;
    --text-white: #ffffff;
  }
  * { box-sizing: border-box; margin: 0; padding: 0; }
  html, body {
    width: 1200px; height: 900px; overflow: hidden;
    background: var(--page-bg);
    font-family: "Comic Neue", "Comic Sans MS", cursive;
  }
  .board { position: relative; width: 1200px; height: 900px; }

  .screen-label {
    position: absolute; top: 92px; width: 256px; text-align: center;
    font-size: 18px; font-weight: 700; color: var(--label-blue); letter-spacing: 0.5px;
  }

  .screen {
    position: absolute; top: 256px; width: 256px; height: 380px;
    border: 10px solid var(--frame-yellow);
    background: linear-gradient(160deg, var(--screen-blue-light) 0%, var(--screen-blue) 45%, var(--screen-blue-deep) 100%);
    overflow: hidden;
  }
  .screen--splash { left: 120px; }
  .screen--menu   { left: 467px; }
  .screen--quiz   { left: 830px; }

  .app-title {
    position: absolute; left: 0; right: 0; text-align: center;
    font-weight: 700; font-size: 26px; color: var(--frame-yellow); line-height: 1;
  }
  .screen--menu .app-title, .screen--quiz .app-title { top: 26px; }
  .screen--splash .app-title { top: 88px; }

  .splash-art {
    position: absolute; left: 30px; top: 124px; width: 176px; height: 150px;
    border-radius: 50%;
    background: radial-gradient(circle at 50% 55%, #f26a1b 0%, #e0431a 35%, #6a5bff 70%, rgba(61,155,255,0) 100%);
  }

  .menu-button {
    position: absolute; left: 34px; width: 188px; height: 36px;
    background: var(--button-white); border: 4px solid var(--frame-yellow); border-radius: 18px;
    display: flex; align-items: center; justify-content: center; gap: 14px;
    font-size: 19px; font-weight: 700; color: var(--ink-dark);
  }
  .menu-button svg { width: 16px; height: 18px; }
  .time-limit {
    position: absolute; right: 8px; display: flex; align-items: center; gap: 5px;
    font-size: 10px; font-weight: 700; color: var(--text-white);
  }
  .time-limit svg { width: 13px; height: 13px; }

  .text-link {
    position: absolute; right: 14px; bottom: 6px; display: flex; align-items: center; gap: 8px;
    font-size: 15px; font-weight: 700; color: var(--text-white);
  }
  .text-link svg { width: 11px; height: 12px; }

  .equation {
    position: absolute; top: 76px; left: 0; right: 0; text-align: center;
    font-size: 28px; font-weight: 700; color: var(--text-white); letter-spacing: 2px;
  }
  .equation .answer { display: inline-block; width: 62px; border-bottom: 3px solid var(--text-white); }

  .keypad { position: absolute; left: 0; top: 0; width: 100%; height: 100%; }
  .key {
    position: absolute; width: 42px; height: 42px; border-radius: 50%;
    background: var(--button-white); border: 5px solid var(--frame-yellow);
    display: flex; align-items: center; justify-content: center;
    font-size: 22px; font-weight: 700; color: var(--ink-dark);
  }
  .key-delete { position: absolute; width: 42px; height: 30px; }
</style>
</head>
<body>
<main class="board">
  <p class="screen-label" style="left:120px">screen 1</p>
  <p class="screen-label" style="left:467px">screen 2</p>
  <p class="screen-label" style="left:830px">screen 5</p>

  <!-- Splash -->
  <section class="screen screen--splash">
    <h1 class="app-title">Sum Rocket Drills</h1>
    <div class="splash-art" role="img" aria-label="Alarm clock illustration with plus, minus, multiply and divide symbols and numbers around it"></div>
  </section>

  <!-- Menu -->
  <section class="screen screen--menu">
    <h1 class="app-title">Sum Rocket Drills</h1>

    <div class="menu-button" style="top:97px">Quick Start <svg viewBox="0 0 16 18"><path d="M1 1 L15 9 L1 17 Z" fill="#14213d"/></svg></div>
    <div class="time-limit" style="top:142px"><svg viewBox="0 0 14 14"><circle cx="7" cy="7" r="6" fill="none" stroke="#fff" stroke-width="1.6"/><path d="M7 3.5 V7 H10" fill="none" stroke="#fff" stroke-width="1.6"/></svg>5 minutes</div>

    <div class="menu-button" style="top:175px">Quick Start 2 <svg viewBox="0 0 16 18"><path d="M1 1 L15 9 L1 17 Z" fill="#14213d"/></svg></div>
    <div class="time-limit" style="top:220px"><svg viewBox="0 0 14 14"><circle cx="7" cy="7" r="6" fill="none" stroke="#fff" stroke-width="1.6"/><path d="M7 3.5 V7 H10" fill="none" stroke="#fff" stroke-width="1.6"/></svg>6½ minutes</div>

    <div class="menu-button" style="top:253px">Quick Start 3 <svg viewBox="0 0 16 18"><path d="M1 1 L15 9 L1 17 Z" fill="#14213d"/></svg></div>
    <div class="time-limit" style="top:298px"><svg viewBox="0 0 14 14"><circle cx="7" cy="7" r="6" fill="none" stroke="#fff" stroke-width="1.6"/><path d="M7 3.5 V7 H10" fill="none" stroke="#fff" stroke-width="1.6"/></svg>8 minutes</div>

    <div class="text-link">For Parents <svg viewBox="0 0 11 12"><path d="M0 0 L11 6 L0 12 Z" fill="#fff"/></svg></div>
  </section>

  <!-- Question -->
  <section class="screen screen--quiz">
    <h1 class="app-title">Sum Rocket Drills</h1>
    <p class="equation">7 × 5 = <span class="answer">35</span></p>

    <div class="keypad">
      <div class="key" style="left:39px;top:131px">1</div>
      <div class="key" style="left:94px;top:131px">2</div>
      <div class="key" style="left:149px;top:131px">3</div>
      <div class="key" style="left:39px;top:178px">4</div>
      <div class="key" style="left:94px;top:178px">5</div>
      <div class="key" style="left:149px;top:178px">6</div>
      <div class="key" style="left:39px;top:225px">7</div>
      <div class="key" style="left:94px;top:225px">8</div>
      <div class="key" style="left:149px;top:225px">9</div>
      <div class="key" style="left:94px;top:272px">0</div>
      <svg class="key-delete" style="left:150px;top:278px" viewBox="0 0 42 30" aria-label="Delete">
        <path d="M12 2 H40 V28 H12 L2 15 Z" fill="#fff" stroke="#ffe600" stroke-width="4" stroke-linejoin="round"/>
        <path d="M20 9 L31 21 M31 9 L20 21" stroke="#14213d" stroke-width="2.6" stroke-linecap="round"/>
      </svg>
    </div>

    <div class="text-link">Next <svg viewBox="0 0 11 12"><path d="M0 0 L11 6 L0 12 Z" fill="#fff"/></svg></div>
  </section>
</main>
</body>
</html>
```